Business Cards and Stationery
Vellomar Development Company
I need single sided standard sized Business Card [3.5" x 2"]
Not sure. Use something compatible with logo.
Professional
Xxxx Xxxxxxx
President
12345 Xxxxxxxxx Xxxxx
Xxxxxxxxx, Xxxxxxxxxx 12345
xxxxxxxxxxx@xxxxxxxxx.xxx
Contractor's License No. 123456
Not that the information will serve as placeholders until the project is awarded and finalized. Actual information will be provided to create final source files.

```html
<!DOCTYPE html>
<html lang="en">
<head>
<meta charset="utf-8">
<title>Vellomar Development Company — Stationery</title>
<link href="https://fonts.googleapis.com/css2?family=Open+Sans:wght@400;600;700&display=swap" rel="stylesheet">
<style>
  :root{
    --navy:#2c2a63;
    --navy-deep:#1d1b46;
    --navy-soft:#4a4890;
    --paper:#ffffff;
    --ink:#3d3d4a;
    --ink-light:#8a8a99;
    --ground:#e9e7ec;
    --faint:#e8e8ef;
  }
  *{box-sizing:border-box;margin:0;padding:0}
  html,body{width:1200px;height:840px;overflow:hidden}
  body{background:var(--ground);font-family:"Open Sans",Arial,sans-serif;color:var(--ink);position:relative}
  .sheet{position:absolute;background:var(--paper);overflow:hidden;box-shadow:0 2px 8px rgba(0,0,0,.18)}
  .swoosh{position:absolute;left:0;top:0}
  .brand{position:absolute;display:flex;align-items:center;gap:6px}
  .brand-dot{border-radius:50%;background:var(--paper);border:3px solid var(--navy)}
  .brand-name{font-weight:700;color:var(--navy);letter-spacing:.5px;line-height:1}
  .contact-block{position:absolute;font-size:6px;line-height:1.5;color:var(--ink-light)}
  /* letterhead */
  .letterhead{left:48px;top:60px;width:396px;height:744px}
  .letterhead .brand{left:92px;top:40px}
  .letterhead .brand-dot{width:30px;height:30px}
  .letterhead .brand-name{font-size:26px}
  .letterhead .contact-block{right:26px;top:20px;text-align:left}
  .letter-body{position:absolute;left:34px;right:34px;top:128px;font-size:7.5px;line-height:1.6;color:var(--ink)}
  .letter-body p{margin-bottom:11px}
  .signature{width:60px;height:26px;background:linear-gradient(90deg,#e2e2ea,#cfcfdb);margin:4px 0 4px;border-radius:3px}
  /* envelope */
  .envelope{left:600px;top:72px;width:552px;height:288px}
  .envelope .brand{left:108px;top:58px}
  .envelope .brand-dot{width:36px;height:36px}
  .envelope .brand-name{font-size:30px}
  .envelope .contact-block{right:28px;top:20px}
  .envelope .return{left:88px;top:190px;font-size:8px;color:var(--ink)}
  .faint-circle{position:absolute;right:50px;top:96px;width:170px;height:170px;border-radius:50%;background:var(--faint)}
  /* business card front */
  .card-front{left:600px;top:408px;width:228px;height:130px}
  .card-front .brand{left:38px;top:22px}
  .card-front .brand-dot{width:16px;height:16px;border-width:2px}
  .card-front .brand-name{font-size:15px}
  .card-person{position:absolute;left:44px;top:64px;font-size:6.5px;line-height:1.4}
  .card-person strong{font-weight:600;color:var(--navy)}
  .card-contact{position:absolute;left:124px;top:62px;font-size:5.5px;line-height:1.8;color:var(--ink)}
  .card-contact span{display:flex;align-items:center;gap:3px}
  .card-contact svg{width:6px;height:6px;fill:var(--navy)}
  /* business card back */
  .card-back{left:828px;top:576px;width:324px;height:192px;background:radial-gradient(circle at 50% 40%,var(--navy-soft),var(--navy) 55%,var(--navy-deep))}
  .card-back .brand-dot{position:absolute;left:142px;top:52px;width:40px;height:40px;border:none}
  .card-back .web{position:absolute;left:0;right:0;top:150px;text-align:center;font-size:9px;font-weight:600;color:var(--paper);letter-spacing:.5px}
</style>
</head>
<body>

<section class="sheet letterhead" aria-label="Letterhead">
  <svg class="swoosh" width="180" height="120" viewBox="0 0 180 120" aria-hidden="true">
    <path d="M0 0H170C120 20 70 55 0 120Z" fill="var(--navy)"/>
    <path d="M170 0C120 20 70 55 0 120V112C66 52 114 18 160 0Z" fill="var(--navy-soft)"/>
  </svg>
  <div class="brand"><span class="brand-dot"></span><span class="brand-name">VELLOMAR</span></div>
  <div class="contact-block">12345, Street No.4, Spot A<br>City Name, State - 12345<br>T: 000 000 0000 &nbsp; E: info@vellomar.com</div>
  <div class="letter-body">
    <p>Dear<br>Client Name</p>
    <p>We are pleased to confirm the start of our partnership on the new residential project. Our team has reviewed the site plans and prepared a schedule that balances quality, safety and cost for every phase of the work.</p>
    <p>During the coming weeks we will coordinate permits, order materials and meet with the design team to settle the final details. We will share progress reports each Friday so that you can follow every milestone and raise any questions early.</p>
    <p>Thank you for placing your trust in our company. We look forward to building something lasting together and to delivering a home that meets your expectations in every way.</p>
    <p>Yours Truly,<br>Project Manager</p>
    <div class="signature" role="img" aria-label="Handwritten signature"></div>
    <p>R. Calloway</p>
  </div>
</section>

<section class="sheet envelope" aria-label="Envelope">
  <svg class="swoosh" width="220" height="150" viewBox="0 0 220 150" aria-hidden="true">
    <path d="M0 0H210C150 25 85 70 0 150Z" fill="var(--navy)"/>
    <path d="M210 0C150 25 85 70 0 150V140C80 66 140 22 198 0Z" fill="var(--navy-soft)"/>
  </svg>
  <div class="brand"><span class="brand-dot"></span><span class="brand-name">VELLOMAR</span></div>
  <div class="contact-block">12345, Street No.4, Spot A<br>City Name, State - 12345<br>www.vellomar.com</div>
  <div class="contact-block return">12345, Street No.4, Spot A<br>City Name, State - 12345<br>www.vellomar.com</div>
  <div class="faint-circle" aria-hidden="true"></div>
</section>

<section class="sheet card-front" aria-label="Business card front">
  <svg class="swoosh" width="80" height="60" viewBox="0 0 80 60" aria-hidden="true">
    <path d="M0 0H76C54 10 30 28 0 60Z" fill="var(--navy)"/>
  </svg>
  <div class="brand"><span class="brand-dot"></span><span class="brand-name">VELLOMAR</span></div>
  <div class="card-person"><strong>Contractor Name</strong><br>President</div>
  <div class="card-contact">
    <span><svg viewBox="0 0 10 10"><path d="M2 1l2 2-1 1.5c.8 1.5 1.5 2.2 3 3L7.5 6l2 2-1.5 1.5C4 9 1 6 .5 1.5Z"/></svg>000 000 0000</span>
    <span><svg viewBox="0 0 10 10"><path d="M5 0a3.5 3.5 0 0 1 3.5 3.5C8.5 6 5 10 5 10S1.5 6 1.5 3.5A3.5 3.5 0 0 1 5 0Zm0 2a1.5 1.5 0 1 0 0 3 1.5 1.5 0 0 0 0-3Z"/></svg>12345, Street No.4</span>
    <span><svg viewBox="0 0 10 10"><path d="M0 2h10v6H0Zm1 1v.3l4 2.5 4-2.5V3Z"/></svg>info@vellomar.com</span>
    <span><svg viewBox="0 0 10 10"><circle cx="5" cy="5" r="4"/></svg>License No. 123456</span>
  </div>
</section>

<section class="sheet card-back" aria-label="Business card back">
  <span class="brand-dot"></span>
  <div class="web">www.vellomar.com</div>
</section>

</body>
</html>
```